Thornwell Building Company - advertisement poster

I am looking to print some canvas signs to advertise my general contracting company, Thornwell Building Company. The sign will measure 6' long x 3' high so the size should match that ratio. I already have a logo icon, which is the Letter 'A' and some trees that I would like to incorporate, see attached. I would also like the to have the following information listed:
1) phone number: 472-318-6095
2) email: thornwellbuildingcompany@mailvistra.net
3) website: thornwellbuildingcompany.com
4) Lic#5386204
5) I want to use this text: "BUILD WITH THE T-CREW!"

The ad should be relatively simple and clean. Black and Green are my company colors. I am open to creative ideas!

Target Market(s)

People looking to renovate their homes

Industry/Entity Type

Construction

Colors
59FF00
82FF00
B8FF75
E3FFCB
F4FFEA

Requirements
Must have
• Must have my company logo
Should not have
• No photos or complex graphics

```html
<!DOCTYPE html>
<html lang="en">
<head>
<meta charset="utf-8">
<title>Thornwell Building Company – Banner</title>
<link rel="stylesheet" href="https://fonts.googleapis.com/css2?family=Orbitron:wght@400;500;700;900&family=Quicksand:wght@500&display=swap">
<style>
  :root {
    --green: #71b246;
    --black: #000000;
    --charcoal: #191919;
    --white: #ffffff;
    --page: #ffffff;
  }
  html, body {
    margin: 0;
    padding: 0;
    width: 1200px;
    height: 963px;
    overflow: hidden;
    background: var(--page);
  }
  .banner {
    position: absolute;
    left: 162px;
    top: 254px;
    width: 886px;
    height: 443px;
    background: var(--black);
    overflow: hidden;
    font-family: "Orbitron", sans-serif;
  }
  .banner-backdrop {
    position: absolute;
    inset: 0;
  }
  .headline {
    position: absolute;
    left: 57px;
    top: 124px;
    margin: 0;
    color: var(--white);
    font-weight: 900;
    font-size: 53px;
    line-height: 67px;
    letter-spacing: 4px;
  }
  .headline span { display: block; }
  .phone {
    position: absolute;
    right: 46px;
    top: 36px;
    color: var(--green);
    font-weight: 500;
    font-size: 19px;
    letter-spacing: 2.5px;
  }
  .contact {
    position: absolute;
    left: 55px;
    top: 389px;
    margin: 0;
    padding: 0;
    list-style: none;
    font-family: "Quicksand", sans-serif;
    font-weight: 500;
    font-size: 13px;
    letter-spacing: 1.1px;
    color: var(--green);
  }
  .contact li {
    display: flex;
    align-items: center;
    height: 21px;
  }
  .contact svg {
    width: 14px;
    height: 14px;
    margin-right: 9px;
    flex: none;
  }
  .brand-mark {
    position: absolute;
    left: 629px;
    top: 196px;
    width: 56px;
    height: 56px;
    background: var(--green);
  }
  .brand-estd {
    position: absolute;
    top: 243px;
    width: 56px;
    height: 21px;
    line-height: 21px;
    text-align: center;
    font-size: 11px;
    font-weight: 500;
    letter-spacing: 3px;
    padding-left: 3px;
    box-sizing: border-box;
    color: var(--white);
    border-top: 1px solid var(--green);
    border-bottom: 1px solid var(--green);
  }
  .brand-estd.left { left: 486px; }
  .brand-estd.right { left: 771px; }
  .brand-name {
    position: absolute;
    left: 440px;
    width: 434px;
    top: 292px;
    margin: 0;
    text-align: center;
    line-height: 1;
  }
  .brand-name .primary {
    display: block;
    color: var(--white);
    font-weight: 900;
    font-size: 46px;
    letter-spacing: 1px;
  }
  .brand-name .secondary {
    display: block;
    margin-top: 6px;
    color: var(--green);
    font-weight: 700;
    font-size: 19px;
    letter-spacing: 7px;
    padding-left: 7px;
  }
  .license {
    position: absolute;
    left: 460px;
    width: 394px;
    top: 389px;
    text-align: center;
    color: var(--green);
    font-weight: 500;
    font-size: 15px;
    letter-spacing: 2px;
    text-transform: uppercase;
  }
</style>
</head>
<body>
  <section class="banner">
    <svg class="banner-backdrop" viewBox="0 0 886 443" width="886" height="443" aria-hidden="true">
      <polygon points="0,0 530,0 401,183 467,183 363,329 434,329 352,443 0,443" fill="var(--charcoal)"/>
      <polygon points="0,0 230,0 0,330" fill="var(--green)"/>
      <polyline points="530,0 401,183 467,183 363,329 434,329 352,443" fill="none" stroke="var(--green)" stroke-width="1.6"/>
    </svg>

    <h1 class="headline">
      <span>BUILD</span>
      <span>WITH THE</span>
      <span>T-CREW!</span>
    </h1>

    <div class="phone">472-318-6095</div>

    <ul class="contact">
      <li>
        <svg viewBox="0 0 16 16" aria-hidden="true"><rect x="1.5" y="3.5" width="13" height="9" rx="1.5" fill="none" stroke="currentColor" stroke-width="1.4"/><polyline points="2,4.5 8,9 14,4.5" fill="none" stroke="currentColor" stroke-width="1.4"/></svg>
        thornwellbuildingcompany@mailvistra.net
      </li>
      <li>
        <svg viewBox="0 0 16 16" aria-hidden="true"><circle cx="8" cy="8" r="6.5" fill="none" stroke="currentColor" stroke-width="1.3"/><ellipse cx="8" cy="8" rx="3" ry="6.5" fill="none" stroke="currentColor" stroke-width="1.1"/><line x1="1.5" y1="8" x2="14.5" y2="8" stroke="currentColor" stroke-width="1.1"/><line x1="2.5" y1="5" x2="13.5" y2="5" stroke="currentColor" stroke-width="1"/><line x1="2.5" y1="11" x2="13.5" y2="11" stroke="currentColor" stroke-width="1"/></svg>
        thornwellbuildingcompany.com
      </li>
    </ul>

    <div class="brand-mark"></div>
    <div class="brand-estd left">ESTD</div>
    <div class="brand-estd right">2020</div>
    <p class="brand-name">
      <span class="primary">THORNWELL</span>
      <span class="secondary">BUILDING COMPANY</span>
    </p>

    <div class="license">Lic# 5386204</div>
  </section>
</body>
</html>
```